Specialist Medical practice after professional trifold flyer design for patient information brochure

I am the Director of the Hollowbrook Clinic, a specialist medial and surgical practice in Australia. I am after a professional design of a patient information trifold flyer that can be used for web distribution or for commercial printing for upcoming educational event. The design would need to allow change of images and text to be used as template for future topics but have a common brand look across them. Colours would follow the logo, but primarily blue colours for the hollowbrook theme. The inside text needs to be clearly contrasted to the background for easy reading, as often elderly patients. The design would make use of curves or circles, but open for hexagonal, triangle square vector components. I have included an outline for the initial brochure and included images to include. Other stock background images can be used if they increase the impact of the design over included. A winning design is also one that could be modified to a 4 page bi-fold brochure

Target Market(s)

This will be provided to patients in GP practices, podiatry clinics, radiological practices. Aimed at patients to read and be compelled to look to site or get consultation with me

Industry/Entity Type

Medical

Font styles to use
Serif
Sans Serif

Colors
33a6d7
0355a3
86cfc6
cedeed
0292cd
85cae6

Requirements
Must have
• The front cover needs to engage the patient to pick up and read- yes I have a painful ankle and want to find out more. the goal for the inside is to provide the options but be able to direct to website for more info - website currently undergoing upgrade. After professional modern look. Not bright contrasting colours like many advertising brochures. Needs to able to have images and text changed but following same look to create new topics
Nice to have
• The focus is a Tri-fold brochure. Nice to be able to modify to bifold. A winning design would even offer both, or submit separate bifold and trifold. I am open to different versions of similar look. (eg option of brochure with curved elements, triangular or square, or hexagonal.
Should not have
• To many contrasting colours. Text must be easily read on background, either white or coloured background texture with transparency

```html
<!DOCTYPE html>
<html lang="en">
<head>
<meta charset="utf-8">
<title>Hollowbrook Clinic – Trifold Brochure</title>
<link href="https://fonts.googleapis.com/css2?family=Roboto+Slab:wght@500;700&family=Lora:ital,wght@1,500&family=Lato:wght@400;700&display=swap" rel="stylesheet">
<style>
:root{
  --page:#e9ebee;
  --paper:#ffffff;
  --paper-soft:#f1f2f4;
  --blue:#33a6d7;
  --blue-mid:#0292cd;
  --blue-deep:#1a7fb8;
  --navy:#0355a3;
  --ink:#5a6470;
  --ink-soft:#8a939c;
  --photo-light:#dfe6ec;
  --photo-mid:#b9c6d2;
}
*{margin:0;padding:0;box-sizing:border-box}
html,body{width:1200px;height:800px;overflow:hidden;background:var(--page)}
body{position:relative;font-family:'Lato',sans-serif;color:var(--ink)}
.panel{position:absolute;top:130px;width:240px;height:540px;background:var(--paper);overflow:hidden;box-shadow:0 2px 10px rgba(0,0,0,.08)}
.panel svg.shapes{position:absolute;left:0;top:0}
.inside-left{left:70px;background:var(--paper-soft)}
.inside-middle{left:310px}
.inside-right{left:550px}
.cover{left:880px}
.serif-head{font-family:'Roboto Slab',serif;color:var(--navy);font-weight:700}
.care-title{position:absolute;left:22px;top:40px;font-size:15px}
.care-list{position:absolute;left:22px;top:66px;width:200px;list-style:none;font-size:7.5px;line-height:13px;color:var(--ink-soft)}
.care-list li{padding-left:12px;position:relative}
.care-list li::before{content:"";position:absolute;left:0;top:3px;width:6px;height:3px;border-left:1.5px solid var(--navy);border-bottom:1.5px solid var(--navy);transform:rotate(-45deg)}
.service-photo{position:absolute;left:22px;top:362px;width:76px;height:76px;border-radius:50%;border:3px solid var(--paper);background:radial-gradient(circle at 40% 40%,#f2d6a8,#d8a64f 60%,#b9c6d2)}
.service-list{position:absolute;left:112px;top:350px;list-style:none;color:#fff;font-family:'Roboto Slab',serif;font-size:11px;line-height:20px}
.service-list li::before{content:"\2714";margin-right:7px}
.contact{position:absolute;left:22px;top:468px}
.contact h3{font-size:13px;margin-bottom:3px}
.contact p{font-size:8.5px;line-height:10.5px;color:var(--ink-soft)}
.quote-title{position:absolute;left:24px;top:28px;width:200px;font-family:'Lora',serif;font-style:italic;color:var(--navy);font-size:14px;line-height:17px;text-align:center}
.nurse-photo{position:absolute;left:50px;top:80px;width:150px;height:230px;background:linear-gradient(180deg,var(--photo-light),var(--photo-mid))}
.body-copy{font-size:7px;line-height:10px;color:var(--ink-soft)}
.middle-copy{position:absolute;left:22px;top:350px;width:200px}
.middle-copy p{margin-bottom:10px}
.team-photo{position:absolute;left:0;top:0;width:240px;height:270px;background:linear-gradient(160deg,#f4f7fa,var(--photo-light) 55%,var(--photo-mid))}
.band-title{position:absolute;left:16px;top:282px;width:200px;color:#fff;font-family:'Roboto Slab',serif;font-size:11px;line-height:14px;text-transform:uppercase;transform:rotate(-14.5deg);transform-origin:left top}
.band-copy{position:absolute;left:16px;top:316px;width:175px;color:#fff;font-size:6.5px;line-height:9px;transform:rotate(-14.5deg);transform-origin:left top}
.right-head{position:absolute;left:20px;top:370px;font-size:13px}
.right-copy{position:absolute;left:20px;top:394px;width:200px}
.brand{position:absolute;left:0;top:20px;width:240px;text-align:center}
.brand-mark{display:block;width:26px;height:26px;border-radius:50%;background:var(--navy);margin:0 auto 6px}
.brand-name{font-family:'Lato',sans-serif;font-weight:400;color:var(--blue-mid);font-size:13px}
.cover-photo{position:absolute;left:30px;top:84px;width:180px;height:215px;background:linear-gradient(180deg,var(--photo-light),var(--photo-mid))}
.tagline{position:absolute;left:0;top:300px;width:240px;height:32px;background:var(--blue);color:#fff;font-family:'Lora',serif;font-style:italic;font-size:14px;line-height:32px;text-align:center}
.cover-copy{position:absolute;left:0;top:332px;width:240px;height:150px;background:var(--blue-mid);padding:12px 16px;color:#fff;font-size:7.5px;line-height:10.5px}
.cover-web{position:absolute;left:0;top:482px;width:240px;height:58px;background:var(--blue-deep);color:#fff;font-size:10px;text-align:center;padding-top:12px}
</style>
</head>
<body>

<section class="panel inside-left">
  <svg class="shapes" width="240" height="540" aria-hidden="true">
    <polygon points="0,372 240,318 240,410 0,462" fill="var(--blue)"/>
  </svg>
  <h2 class="serif-head care-title">We Care About:</h2>
  <ul class="care-list">
    <li>Lorem ipsum dolor sit mero moleamet, soluta</li>
    <li>euismod his ea, hlea munere accusamus ullamco</li>
    <li>ore rper quo, utamur sig</li>
    <li>niferumque et duo. Brute inani in pro, in est audire</li>
    <li>Eos rebum dicant constituto ex, vix</li>
    <li>molestiae ne, nam an fugit probatus suscipiantur,</li>
    <li>Dicit quaestio principes ipsum ex, id est alia scriptore</li>
    <li>mdefinitiones. Assum legimuse</li>
  </ul>
  <div class="service-photo" role="img" aria-label="Photo of a smiling family of three"></div>
  <ul class="service-list">
    <li>Health</li>
    <li>Hygenic</li>
    <li>Consultation</li>
  </ul>
  <div class="contact">
    <h3 class="serif-head">Contact us:</h3>
    <p>Ph: 03 9555 0141</p>
    <p>Web: www.hollowbrookclinic.com.au</p>
    <p>Skype: hollowbrook.clinic</p>
    <p>Fax: 03 9555 0142</p>
    <p>E-mail: care@hollowbrookclinic.com.au</p>
  </div>
</section>

<section class="panel inside-middle">
  <svg class="shapes" width="240" height="540" aria-hidden="true">
    <polygon points="0,262 240,208 240,290 0,344" fill="var(--blue)"/>
  </svg>
  <h2 class="quote-title">“ Live a Healty Perfact Life that makes you Fill “</h2>
  <div class="nurse-photo" role="img" aria-label="Photo of a nurse holding a clipboard"></div>
  <div class="middle-copy body-copy">
    <p>Lorem ipsum dolor sit mero moleamet, soluta euismod his ea, hlea munere accusamus ullamco detore rper quo, utamur sig niferumque et duo. Brute inani in pro, in est audire delicata. Eos rebum dicant constituto ex, vix hinc posse molestiae ne, nam an fugit probatus suscipiantur. Dicit quaestio principes ipsum ex, id est alia scriptorem definitiones. Assum legimuse ferentur nam ut.</p>
    <p>nam an fugit probatus suscipiantur. Dicit quaestio principes ipsum ex, id est alia scriptorem definitiones. Assum legimuse ferentur nam ut.</p>
  </div>
</section>

<section class="panel inside-right">
  <div class="team-photo" role="img" aria-label="Photo of a team of three doctors in a clinic"></div>
  <svg class="shapes" width="240" height="540" aria-hidden="true">
    <polygon points="0,262 240,200 240,300 0,362" fill="var(--blue)"/>
    <polygon points="0,362 240,300 240,540 0,540" fill="var(--paper)"/>
  </svg>
  <h2 class="band-title">Live a healty perfact life that makes you fill</h2>
  <p class="band-copy">Lorem ipsum dolor sit mero moleamet, soluta euismod his ea, hlea munere accusamus ullamco detore rper quo, utamur sig niferumque et duo.</p>
  <h3 class="serif-head right-head">Expert Doctors</h3>
  <p class="right-copy body-copy">Lorem ipsum dolor sit mero moleamet, soluta euismod his ea, hlea munere accusamus ullamco detore rper quo, utamur sig niferumque et duo. Brute inani in pro, in est audire delicata. Eos rebum dicant constituto ex, vix hinc posse molestiae ne, nam an fugit probatus suscipiantur.</p>
</section>

<section class="panel cover">
  <div class="brand">
    <span class="brand-mark" aria-hidden="true"></span>
    <span class="brand-name">Hollowbrook Clinic</span>
  </div>
  <div class="cover-photo" role="img" aria-label="Photo of a nurse holding a clipboard"></div>
  <p class="tagline">“ The name of Assurity “</p>
  <p class="cover-copy">Lorem ipsum dolor sit mero moleamet, soluta euismod his ea, hlea munere accusamus ullamco detore rper quo, utamur sig niferumque et duo. Brute inani in pro, in est audire delicata. Eos rebum dicant constituto ex, vix hinc posse molestiae ne, nam an fugit probatus suscipiantur. Dicit quaestio principes ipsum ex, id est alia scriptorem definitiones. Assum legimuse ferentur nam ut.</p>
  <p class="cover-web">www.hollowbrookclinic.com.au</p>
</section>

</body>
</html>
```